Wordpress Design Project

We are an online jewellery business currently trading entirely online through internet auctions.

We are revamping our online operations. We want to launch our website. Which will incorporate extensive social media integration. Chatterloop, Blogging to chatterloop as well as Clipwall. These need to be linked (some and/or interactive).

We want to collect subscriptions and collate emails/info.

There may also be video uploads of our stock.

Whilst we are Sydney based we see ourselves as a global business.

We sell High End exclusive designer jewellery.
Often bespoke pieces of diamond jewellery.

Words that some up our brand personality
Savvy, Stylish, Confident, Approachable

About our style
Ensuring not only that our designs and jewellery have a certain sense of classic or fashion-driven style, but expressing style and beauty through all touch points. We understand that style is not only about what you wear, but how you carry yourself.

About our company mission
Make precious jewellery an affordable luxury for stylish, savvy buyers
Create products that we're proud to sell and that customers desire, treasure and proudly wear.

KEY FOCUS/OUTCOME:

We require a stylish, clean, visually easy to navigate website. Main aim of the site is to showcase products. Not a shop per se. Ultimate goal is to engage the viewer to ask us to make something special for them. Not a huge budget. WE are a small business. But we make beautiful fine jewellery. Focus on Blog, social media interactions important, Innovative WORDPRESS design. Think special. We want to be inspired as we are inspired by some of the links we've presented here. They give a great overall feel of what we are looking for.

We require full implementation to be delivered.

http://www.vastrelmo.com/
http://www.rovendacycles.com/
http://www.tarvishale.com/cocktails/
www.kelpora.ch
http://www.ventulise.fr/en

SEO expertise as well as adaptation across all mobile devices/tablets.

Industry/Entity Type

Internet

Requirements
Must have
• Social Media, Blog, unique design (not same-same) Has to feel bespoke. 48 hour "buy it now" feature. Like a daily deal function with the ability to check out through CoinDrift. One high ticket item per day. Easy for us to manipulate/upload to website. User friendly.
Fast website. Not slow.
Should not have
• -should not look like a traditional shopping cart.

```html
<!DOCTYPE html>
<html lang="en">
<head>
<meta charset="utf-8">
<title>Verimonte Designer Jewellery</title>
<link rel="stylesheet" href="https://fonts.googleapis.com/css2?family=Playfair+Display:wght@400;700&family=Montserrat:wght@300;400;600&display=swap">
<style>
:root{
  --page:#3a3a3a;
  --tile:#000000;
  --ink:#ffffff;
  --muted:#9a9a9a;
  --soft:#cfcfcf;
  --rule:#2c2c2c;
  --accent:#d63bff;
  --serif:"Playfair Display", Georgia, serif;
  --sans:"Montserrat", Arial, sans-serif;
}
*{margin:0;padding:0;box-sizing:border-box}
html,body{width:977px;height:1200px;overflow:hidden;background:var(--page)}
body{position:relative;font-family:var(--sans);color:var(--ink)}
.abs{position:absolute}

/* header */
.brand{left:28px;top:15px;width:138px}
.brand-name{font-family:var(--serif);font-size:21px;letter-spacing:.5px;line-height:1;border-bottom:2px solid var(--ink);padding-bottom:3px}
.brand-tag{font-family:var(--serif);font-size:7px;text-align:right;margin-top:2px}
.nav{right:27px;top:27px;display:flex;gap:22px;font-family:var(--serif);font-weight:700;font-size:10.5px;letter-spacing:.2px}

/* tiles */
.tile{position:absolute;background:var(--tile);overflow:hidden}
.photo{position:absolute;inset:0}
.caption{font-family:var(--serif);font-weight:700}

.hero-text{left:259px;top:280px;font-size:27px;line-height:30px}
.hero-text .accent{color:var(--accent)}
.ring-caption{left:10px;top:145px;font-size:15px}

/* blog */
.blog-head{left:13px;top:197px;font-size:26px}
.blog-list{left:10px;top:243px;width:210px;list-style:none;border-top:1px solid var(--rule)}
.blog-list li{border-bottom:1px solid var(--rule);padding:7px 0 9px}
.blog-date{font-size:16px;font-weight:300;color:var(--muted);display:block;line-height:18px}
.blog-sum{font-size:9.5px;color:var(--soft);line-height:12px;display:block}
.blog-more{left:11px;top:438px;font-family:var(--serif);font-size:15px;color:var(--muted)}

/* deal */
.deal{left:257px;top:42px}
.deal-title{font-family:var(--serif);font-weight:700;font-size:22px;line-height:26px}
.deal-item{font-family:var(--serif);font-weight:700;font-size:15px;margin-top:2px}
.countdown{display:flex;align-items:center;gap:4px;margin-top:12px}
.count-box{background:var(--ink);color:var(--tile);font-family:var(--serif);font-weight:700;font-size:38px;width:47px;height:48px;display:flex;align-items:center;justify-content:center;letter-spacing:-1px}
.count-sep{font-family:var(--serif);font-weight:700;font-size:24px}
.deal-link{font-family:var(--serif);font-weight:700;font-size:14px;color:var(--soft);margin-top:8px;display:block}

/* social bar */
.bar{left:13px;top:1035px;width:950px;height:43px;background:var(--tile);display:flex;align-items:center}
.social{display:flex;align-items:center;width:475px;height:100%;border-right:2px solid var(--page);padding-left:13px}
.social-title{font-family:var(--serif);font-weight:700;font-size:20px;margin-right:12px}
.stat{display:flex;align-items:center;gap:5px;padding:0 10px;border-left:1px solid #444;height:26px}
.stat-dot{width:9px;height:9px;border-radius:50%;background:var(--ink)}
.stat-num{font-size:10px;font-weight:600;line-height:11px}
.stat-label{font-size:7.5px;color:var(--soft);line-height:9px}
.subscribe{display:flex;align-items:center;padding-left:11px;gap:10px}
.subscribe-title{font-family:var(--serif);font-weight:700;font-size:17px}
.subscribe-form{display:flex;align-items:center;justify-content:space-between;background:var(--ink);width:235px;height:28px;padding:0 6px}
.subscribe-input{font-family:var(--serif);font-size:11px;color:#b5b5b5}
.subscribe-btn{font-family:var(--serif);font-weight:700;font-size:13px;color:var(--tile)}

/* footer */
.footer{left:13px;top:1093px;width:950px;height:90px;background:var(--tile)}
.footer-links{left:23px;top:22px;display:flex;gap:28px;font-family:var(--serif);font-weight:700;font-size:10.5px;color:var(--soft)}
.footer-rule{left:23px;right:23px;top:58px;height:1px;background:var(--rule)}
.footer-small{left:26px;top:69px;display:flex;gap:18px;font-size:7.5px;color:var(--soft)}
.footer-brand{right:25px;top:14px;width:106px;color:var(--muted)}
.footer-brand .brand-name{font-size:15px;border-bottom:1px solid var(--muted)}
.footer-brand .brand-tag{font-size:6px}
.copyright{right:23px;top:70px;font-size:7px;color:#555}
</style>
</head>
<body>

<header>
  <div class="abs brand">
    <div class="brand-name">VERIMONTE</div>
    <div class="brand-tag">designer jewellery</div>
  </div>
  <nav class="abs nav">
    <span>COLLECTION GALLERY</span><span>ABOUT US</span><span>BLOG</span><span>EDUCATION</span><span>BUYING FROM US</span><span>TESTIMONIALS</span><span>48 HOUR PRODUCT OFFER</span>
  </nav>
</header>

<main>
  <section class="tile" style="left:13px;top:71px;width:469px;height:469px">
    <div class="photo" role="img" aria-label="Square-cut amethyst cocktail ring with diamond pavé halo on black" style="background:radial-gradient(circle at 36% 30%,#7b2fb0 0,#3a1456 22%,#0a0a0a 48%,#000 70%)"></div>
    <p class="abs caption hero-text">Our pieces are<br>inspired by what<br>appeals to the eye<br>and the <span class="accent">heart</span></p>
  </section>

  <section class="tile" style="left:494px;top:71px;width:228px;height:228px">
    <div class="photo" role="img" aria-label="White gold solitaire diamond ring with reflection" style="background:radial-gradient(circle at 50% 35%,#8a8a8a 0,#2a2a2a 30%,#000 62%)"></div>
    <p class="abs caption ring-caption">White Gold Diamond Ring</p>
  </section>

  <section class="tile" style="left:735px;top:71px;width:228px;height:228px">
    <div class="photo" role="img" aria-label="Silver chain necklaces with polished and pavé ball pendants" style="background:radial-gradient(circle at 60% 55%,#9a9a9a 0,#4a4a4a 30%,#111 70%)"></div>
  </section>

  <section class="tile" style="left:494px;top:312px;width:228px;height:228px">
    <div class="photo" role="img" aria-label="Emerald ring with diamond halo displayed on a frosted glass hand" style="background:radial-gradient(circle at 30% 55%,#d9d9d9 0,#8c8c8c 25%,#111 60%,#000 80%)"></div>
  </section>

  <section class="tile" style="left:735px;top:312px;width:228px;height:228px">
    <div class="photo" role="img" aria-label="Yellow gold ring set with a cluster of diamonds" style="background:radial-gradient(circle at 50% 40%,#a58d63 0,#4b3f2b 30%,#0a0a0a 65%)"></div>
  </section>

  <section class="tile" style="left:13px;top:554px;width:228px;height:468px">
    <div class="abs" role="img" aria-label="Princess-cut diamond engagement ring" style="left:0;top:0;width:228px;height:180px;background:radial-gradient(circle at 45% 40%,#8a8a8a 0,#2b2b2b 30%,#000 65%)"></div>
    <h2 class="abs caption blog-head">Blogposts</h2>
    <ul class="abs blog-list">
      <li><span class="blog-date">24/07/2013</span><span class="blog-sum">Curabitur condimentum neque in leo hendrerit, at lacinia lacus fringilla.</span></li>
      <li><span class="blog-date">30/06/2013</span><span class="blog-sum">Morbi volutpat purus non lectus mollis, sed consequat risus lobortis.</span></li>
      <li><span class="blog-date">15/06/2013</span><span class="blog-sum">Mauris eget massa elementum, pulvinar elit non, convallis nisi.</span></li>
    </ul>
    <span class="abs blog-more">read more posts</span>
  </section>

  <section class="tile" style="left:254px;top:554px;width:228px;height:228px">
    <div class="photo" role="img" aria-label="Black pearl ring in a gold and diamond flower setting" style="background:radial-gradient(circle at 50% 38%,#7a6a4e 0,#2a261e 22%,#000 55%)"></div>
  </section>

  <section class="tile" style="left:494px;top:554px;width:469px;height:228px">
    <div class="photo" role="img" aria-label="Steel wristwatch with diamond bezel and black dial" style="background:radial-gradient(ellipse at 52% 50%,#1a1a1a 0,#7d7d7d 30%,#3a3a3a 55%,#050505 80%)"></div>
  </section>

  <section class="tile" style="left:254px;top:795px;width:228px;height:227px">
    <div class="photo" role="img" aria-label="White pearl pendant in a twisted gold and diamond frame" style="background:radial-gradient(circle at 52% 55%,#e8e6e0 0,#8a7a5c 25%,#1a1610 50%,#000 70%)"></div>
  </section>

  <section class="tile" style="left:494px;top:795px;width:469px;height:227px">
    <div class="abs" role="img" aria-label="Platinum princess-cut engagement ring" style="left:0;top:0;width:240px;height:227px;background:radial-gradient(circle at 50% 45%,#8f8f8f 0,#2e2e2e 30%,#000 62%)"></div>
    <div class="abs deal">
      <h2 class="deal-title">TODAY’s DEAL</h2>
      <p class="deal-item">Platinum Engagement Ring.</p>
      <div class="countdown">
        <span class="count-box">15</span><span class="count-sep">:</span>
        <span class="count-box">51</span><span class="count-sep">:</span>
        <span class="count-box">35</span>
      </div>
      <span class="deal-link">LEARN MORE</span>
    </div>
  </section>
</main>

<section class="abs bar">
  <div class="social">
    <span class="social-title">WE’RE SOCIAL</span>
    <div class="stat"><span class="stat-dot"></span><div><div class="stat-num">856</div><div class="stat-label">Clipwall followers</div></div></div>
    <div class="stat"><span class="stat-dot"></span><div><div class="stat-num">2568</div><div class="stat-label">Chatterloop likes</div></div></div>
    <div class="stat"><span class="stat-dot"></span><div><div class="stat-num">2568</div><div class="stat-label">Streamora subscribers</div></div></div>
  </div>
  <div class="subscribe">
    <span class="subscribe-title">Subscribe to latest updates</span>
    <div class="subscribe-form"><span class="subscribe-input">Enter Email here</span><span class="subscribe-btn">SUBSCRIBE</span></div>
  </div>
</section>

<footer class="abs footer">
  <div class="abs footer-links"><span>Custom Care</span><span>Product Information</span><span>Shipping &amp; Delivery</span><span>Returns &amp; Exchanges</span><span>Privacy &amp; Security</span></div>
  <div class="abs footer-brand"><div class="brand-name">VERIMONTE</div><div class="brand-tag">designer jewellery</div></div>
  <div class="abs footer-rule"></div>
  <div class="abs footer-small"><span>FAQ</span><span>Contact Us</span><span>Terms &amp; Conditions</span><span>Sitemap</span></div>
  <div class="abs copyright">© 2013 Copyright Verimonte Designer Jewellery</div>
</footer>

</body>
</html>
```